TELVANO End User Instruction Guide

I need to create a 5 to 7-page instruction guides for customers who purchased a phone system from our company. The document is a quick reference guide that will help end-users learn how to set up and use their new desk phone and software applications. I need the guide to be 3 x 5 or 6 x 8 in size and will fold like a book.

Target Market(s)

Business users / Corvana Desk Phone Users / TelVANO Portal users

Industry/Entity Type

Telecommunications

Font styles to use
Serif

Colors
0758a5
ffffff

Requirements
Must have
• Need to have step-by-step instructions that include the information from the QuickStart guide I provided. I need to see an image of the phone with an arrow pointing to the key on the phone that should be pressed. For example, when checking voicemail the Messages key is pressed and I want to highlight this button or call it out somehow.

I need to have three pages for setup instructions, one page for shortcuts or features codes and our support contacts on the last page.
Nice to have
• I want to have a page for notes that the end-user can use during training. I would also like to have a blank space next to passwords and user ID's so they can be filled out with specific details that are provided during their training. For example, in the voicemail section, I include a default PIN. I would like to leave this blank and let the end-user fill it out during training.
Should not have
• Complex shapes and designs. I like straight lines and a simple easy to understand layout.

```html
<!DOCTYPE html>
<html lang="en">
<head>
<meta charset="utf-8">
<title>TelVANO End-User Quick Start Guide</title>
<link rel="stylesheet" href="https://fonts.googleapis.com/css2?family=Montserrat:wght@700;800&family=Source+Sans+3:wght@400;600;700&display=swap">
<style>
:root{
  --navy:#263c8e;
  --blue:#2f4da3;
  --ink:#333;
  --muted:#555;
  --bar:#353535;
  --paper:#ffffff;
  --bg:#cfd0d1;
  --line:#bfbfbf;
}
*{box-sizing:border-box;margin:0;padding:0}
html,body{width:1200px;height:2476px;overflow:hidden;background:var(--bg)}
body{position:relative;font-family:"Source Sans 3",Arial,sans-serif;color:var(--ink)}
.page{position:absolute;top:0;width:417px;height:555px;background:var(--paper);overflow:hidden}
.spread{position:absolute;left:196px;width:834px;height:555px;box-shadow:0 6px 14px rgba(0,0,0,.25)}
.spread .page.left{left:0}
.spread .page.right{left:417px}
.s1{top:113px}.s2{top:708px}.s3{top:1305px}.s4{top:1913px}

.brand{position:absolute;left:30px;top:26px;display:flex;align-items:center;gap:6px}
.brand .mark{width:14px;height:14px;background:var(--navy)}
.brand .name{font-family:"Montserrat",sans-serif;font-weight:800;font-size:17px;color:var(--navy);letter-spacing:.5px}
.tab{position:absolute;left:198px;top:35px;width:202px;height:19px;background:var(--navy);color:#fff;font-weight:700;font-size:10.5px;line-height:19px;padding-left:30px;clip-path:polygon(10px 0,100% 0,100% 100%,0 100%)}
.foot{position:absolute;left:0;bottom:8px;width:100%;height:18px;background:var(--bar);color:#fff;font-size:7px;font-weight:600;text-align:right;line-height:18px;padding-right:17px}
.content{position:absolute;left:21px;right:16px;top:82px;font-size:7.6px;line-height:1.3}
.step{font-size:13px;color:var(--navy);font-weight:700;margin-bottom:14px}
.step span{font-weight:400}
h3{font-size:9.6px;color:var(--navy);font-weight:700;margin:12px 0 5px}
h4{font-size:7.8px;font-weight:700;margin:6px 0 3px}
p{margin-bottom:4px;text-align:justify}
ul{list-style:none}
li{position:relative;padding-left:9px;margin-bottom:2px}
li::before{content:"•";position:absolute;left:0}
ol.dots{list-style:none}
ol.dots li::before{content:"";top:3px;width:5px;height:5px;border-radius:50%;background:var(--navy)}
.key{display:inline-block;width:9px;height:8px;background:#333;border-radius:1px;vertical-align:middle;margin:0 2px}
.key.light{background:#fff;border:1px solid #444}
b{font-weight:700}

/* cover */
.cover .title{position:absolute;left:22px;top:45px;font-family:"Montserrat",sans-serif;font-weight:800;font-size:31px;line-height:41px;color:#fff;z-index:2}
.cover .brand{left:68px;top:458px}
.cover .brand .mark{width:30px;height:30px}
.cover .brand .name{font-size:33px}
.navyfoot{position:absolute;left:0;bottom:0;width:100%;height:41px;background:var(--navy);color:#fff;font-size:7px;display:flex;gap:14px;align-items:center;padding-left:12px}
.navyfoot i{display:inline-block;width:7px;height:7px;border-radius:50%;background:#fff;margin-right:4px;vertical-align:middle}
.cover-photo{position:absolute;left:200px;top:280px;width:200px;height:140px;border-radius:4px;background:linear-gradient(135deg,#d9dbe0,#b4b8c0)}

/* star code page */
.concept{position:absolute;top:68px;left:21px;right:16px;display:flex;gap:10px;font-size:5px;line-height:1.25}
.concept div{flex:1}
.concept b{color:var(--navy)}
.codes{position:absolute;left:21px;right:16px;top:118px;height:318px;border:1px solid #888;display:flex;font-size:4.4px;line-height:1.35}
.codes .col{flex:1;border-right:1px solid #888}
.codes .col:last-child{border-right:0}
.codes .hd{display:flex;border-bottom:1px solid #888;font-weight:700;font-size:5.2px;padding:3px 2px}
.codes .row{display:flex;padding:0 2px}
.codes .c{width:45px}
.codes .d{flex:1}
.support{position:absolute;left:0;bottom:0;width:100%;height:112px;background:var(--navy);color:#fff}
.support .lbl{position:absolute;left:0;top:0;width:140px;height:22px;background:#fff;clip-path:polygon(0 0,100% 0,92% 100%,0 100%)}
.support .lbl span{position:absolute;left:22px;top:8px;font-size:8.5px;font-weight:700;color:var(--navy)}
.support .lines{position:absolute;left:22px;top:32px;font-size:6.6px;line-height:11.5px;font-weight:600}
.support .navyfoot{height:30px;border-top:1px solid rgba(255,255,255,.3)}

/* portal mock */
.login{position:absolute;left:18px;top:148px;width:90px;height:100px;border:1px solid #ddd;box-shadow:0 1px 3px rgba(0,0,0,.15);padding:6px}
.login .n{font-family:"Montserrat",sans-serif;font-weight:800;font-size:8px;color:var(--navy)}
.login .f{height:6px;background:#eef0f6;border:1px solid #ccd;margin:10px 0 4px}
.login .btn{height:8px;background:var(--blue);margin-top:10px}
.icons{position:absolute;left:45px;top:278px;display:flex;gap:9px}
.icons div{width:28px;height:22px;border:1px solid #bbb;border-radius:3px;background:linear-gradient(#f5f5f5,#ddd)}
.icons div.on{background:linear-gradient(#9fc5ea,#5c94cf)}
.msgs{position:absolute;left:24px;top:318px;width:370px;font-size:4.6px}
.msgs .bar{height:11px;background:linear-gradient(#b8bcc4,#8f949d);color:#fff;font-size:6px;line-height:11px;padding-left:6px}
.msgs .r{display:flex;border-bottom:1px solid #eee;padding:2px 10px}
.msgs .r span{flex:1}

/* app */
.get{position:absolute;left:21px;top:147px;width:114px;height:96px;background:#eee}
.get .g{height:21px;background:#bdbdbd;color:#fff;font-size:10px;font-weight:700;text-align:center;line-height:21px}
.badge{width:74px;height:22px;background:#111;border-radius:3px;margin:9px auto 0}
.appicon{display:inline-block;width:20px;height:20px;border-radius:4px;background:#2e7fc0;vertical-align:middle;margin-left:3px}
.shot{position:absolute;width:92px;height:210px;border-radius:14px;border:1px solid #bbb}
</style>
</head>
<body>

<section class="spread s1">
  <div class="page left codespage">
    <div class="brand"><div class="mark"></div><div class="name">TELVANO</div></div>
    <div class="tab">STAR CODES AND FEATURES</div>
    <div class="concept">
      <div><b>Concept</b><br>Many features in the CloudDesk platform are controlled by dialing the star key in conjunction with a 2 or 3 digit code. The default star codes are listed below. These may be customized per domain by the NetCore Control Tower.</div>
      <div><b>Reserved Number Space</b><br>Certain 3-4 digit extensions should NOT be used. Please be aware of the Reserved Number Space page to avoid any conflicts with dial translations.</div>
    </div>
    <div class="codes">
      <div class="col">
        <div class="hd"><span class="c">STAR CODE</span><span class="d">FEATURE DESCRIPTION</span></div>
        <div class="row"><span class="c">**</span><span class="d">Dynamically Park a Call (in the 701-709 range)</span></div>
        <div class="row"><span class="c">*(parking lot)</span><span class="d">Park a Call (to a specified park ext)</span></div>
        <div class="row"><span class="c">*33(ext)</span><span class="d">Extension Pickup - Answer a call ringing at another extension</span></div>
        <div class="row"><span class="c">*36</span><span class="d">Domain Pickup - Answer a call ringing within the same domain</span></div>
        <div class="row"><span class="c">*37</span><span class="d">Department Pickup - Answer a call ringing within the same department</span></div>
        <div class="row"><span class="c">*38</span><span class="d">Self Pickup - Moves an active call to another extension owned by the same user</span></div>
        <div class="row"><span class="c">*40</span><span class="d">Activate Call Forwarding</span></div>
        <div class="row"><span class="c">*41</span><span class="d">Set Forward Busy Destination to device or external number; auto-attendant must be done in the portal</span></div>
        <div class="row"><span class="c">*42</span><span class="d">Set Forward No Answer Feature</span></div>
        <div class="row"><span class="c">*44</span><span class="d">Hotdesking (Log In) - Requires user login and password</span></div>
        <div class="row"><span class="c">*45</span><span class="d">Disable Call Forwarding (for Hotdesking). This star code is deprecated</span></div>
        <div class="row"><span class="c">*46</span><span class="d">Hotdesking (Log Out) - Requires password of current logged in user</span></div>
        <div class="row"><span class="c">*48</span><span class="d">Ask caller to enter PIN before connecting call</span></div>
        <div class="row"><span class="c">*49</span><span class="d">Ask caller to enter extension before connecting call</span></div>
        <div class="row"><span class="c">*50(ext)</span><span class="d">Auto Answer/Intercom (3 or 4 digit ext). Not with SLA</span></div>
        <div class="row"><span class="c">*55(Parking Lot)</span><span class="d">Retrieve a call from a Call Park Queue</span></div>
        <div class="row"><span class="c">*61</span><span class="d">To Voicemail - Unauthenticated</span></div>
        <div class="row"><span class="c">*62</span><span class="d">To Voicemail - Password Only</span></div>
        <div class="row"><span class="c">*66&lt;10 or 11</span><span class="d">Digit phone number &gt; route call off-net through a carrier instead of staying on network</span></div>
        <div class="row"><span class="c">*67&lt;10 or 11</span><span class="d">Digit phone number &gt; To connection w/ privacy DID 11 digit</span></div>
        <div class="row"><span class="c">*67(ext)</span><span class="d">To User w/ Privacy</span></div>
        <div class="row"><span class="c">*69</span><span class="d">Call Return</span></div>
        <div class="row"><span class="c">*72&lt;10 or 11</span><span class="d">Digit phone or extension &gt; Set Forward Destination to device or external number</span></div>
        <div class="row"><span class="c">*73</span><span class="d">DeActivate Forward</span></div>
      </div>
      <div class="col">
        <div class="hd"><span class="c">STAR CODE</span><span class="d">FEATURE DESCRIPTION</span></div>
        <div class="row"><span class="c">*74</span><span class="d">Activate Night Mode (requires setup)</span></div>
        <div class="row"><span class="c">*75</span><span class="d">DeActivate Night Mode</span></div>
        <div class="row"><span class="c">*78</span><span class="d">Activate Do Not Disturb</span></div>
        <div class="row"><span class="c">*79</span><span class="d">DeActivate Do Not Disturb</span></div>
        <div class="row"><span class="c">*80</span><span class="d">Start Call Recording</span></div>
        <div class="row"><span class="c">*81</span><span class="d">Stop Call Recording</span></div>
        <div class="row"><span class="c">*82</span><span class="d">Pause Call Recording for 1 minute or until *83, whichever comes first</span></div>
        <div class="row"><span class="c">*83</span><span class="d">Resume Call Recording from a paused state</span></div>
        <div class="row"><span class="c">*88</span><span class="d">Make Agent Available for all Queues the Agent is a member of (Online)</span></div>
        <div class="row"><span class="c">*89</span><span class="d">Make Agent Unavailable for all Queues the Agent is a member of (Offline)</span></div>
        <div class="row"><span class="c">*90</span><span class="d">Activate Forward Busy to device or external number; auto-attendant set in the portal</span></div>
        <div class="row"><span class="c">*91</span><span class="d">DeActivate Forward Busy</span></div>
        <div class="row"><span class="c">*92</span><span class="d">Activate Forward No Answer to device or external number set in the portal</span></div>
        <div class="row"><span class="c">*93</span><span class="d">DeActivate Forward No Answer</span></div>
        <div class="row"><span class="c">*97(ext)</span><span class="d">Transfer to a 4-digit Extension</span></div>
        <div class="row"><span class="c">*98(ext)</span><span class="d">Transfer to a 3-digit Extension</span></div>
        <div class="row"><span class="c">*99</span><span class="d">Transfer to Self</span></div>
        <div class="row"><span class="c">Shortcut</span><span class="d">Feature Description</span></div>
        <div class="row"><span class="c">7(ext)</span><span class="d">Transfer a call directly to voicemail (3 or 4 digit extension)</span></div>
        <div class="row"><span class="c">71[0-9]</span><span class="d">Transfer a call to a Call Park Queue in the 710-719 range for parking without callback</span></div>
        <div class="row"><span class="c">72[0-9]</span><span class="d">Transfer a call to a Call Park Queue in the 720-729 range for parking with callback</span></div>
        <div class="row"><span class="c">99(ext)</span><span class="d">Auto Answer/Intercom (3 or 4 digit extension). Not with SLA</span></div>
        <div class="row"><span class="c">099</span><span class="d">Invoke the Account Code feature</span></div>
        <div class="row"><span class="c">5000</span><span class="d">Unregistered Login to VMail (prompted for acct no and password)</span></div>
        <div class="row"><span class="c">5001</span><span class="d">Registered Login to VMail (prompted for password only)</span></div>
        <div class="row"><span class="c">5002</span><span class="d">Hot Desking Sign In</span></div>
        <div class="row"><span class="c">5003</span><span class="d">Request User's PIN, then provides 2nd distinctive prompt (useful for phones in public spaces)</span></div>
      </div>
    </div>
    <div class="support">
      <div class="lbl"><span>SUPPORT NUMBERS</span></div>
      <div class="lines">
        Call/Text Support for Assistance: 555-014-2290<br>
        Text the word "Guide" to 555-014-2291 for a digital copy of this guide and others.<br>
        Visit our resources page at: www.telvanocommunications.com/resources<br>
        For LinkDial resources go to: www.linkdial.com
      </div>
      <div class="navyfoot">
        <span><i></i>support@telvanocommunications.com</span>
        <span><i></i>555-014-2291</span>
        <span><i></i>www.telvanocommunications.com</span>
      </div>
    </div>
  </div>

  <div class="page right cover">
    <svg width="417" height="555" style="position:absolute;left:0;top:0">
      <polygon points="0,0 417,0 360,62 250,150 120,250 0,345" fill="#263c8e"/>
      <polygon points="360,62 417,0 417,320 380,330 170,300 120,250 250,150" fill="#a9aebb" role="img" aria-label="Collage of office team photos set in diamond frames"/>
    </svg>
    <div class="cover-photo" role="img" aria-label="Photo of a Corvana desk phone with touchscreen and handset"></div>
    <div class="title">END USER<br>QUICK START<br>GUIDE</div>
    <div class="brand"><div class="mark"></div><div class="name">TELVANO</div></div>
    <div class="navyfoot">
      <span><i></i>support@telvanocommunications.com</span>
      <span><i></i>555-014-2291</span>
      <span><i></i>www.telvanocommunications.com</span>
    </div>
  </div>
</section>

<section class="spread s2">
  <div class="page left">
    <div class="brand"><div class="mark"></div><div class="name">TELVANO</div></div>
    <div class="tab">END-USER QUICK START GUIDE</div>
    <div class="content">
      <div class="step">STEP 1: <span>Set-Up Your Voicemail</span></div>
      <p>The first time you log in to your mailbox, you are walked through recording your name for the directory and recording your personal greeting. The name recording is for the dial-by-name directory, so when someone enters the first three letters of your last name, it will playback your name recording. The greeting plays when your mailbox is reached. It is essential to make a custom message, as many callers will not leave messages at mailboxes that have generic greetings.</p>
      <h3 style="margin-top:30px">Accessing Voicemail from your Desk Phone</h3>
      <ol class="dots">
        <li>Press the <b>Messages</b> <span class="key light"></span> button on your phone to access your voicemail box, or dial 5001 if you can not identify the voicemail button.</li>
        <li style="margin-top:10px">When prompted, enter your default voicemail pin ________, and then press <span class="key"></span></li>
      </ol>
      <p style="padding-left:15px;margin-top:10px"><b>Note:</b> If you subscribe to multiple mailboxes, press the left or right arrows on the directional pad to select the extension of the voicemail you want to access. Then follow the steps above.</p>
      <h3 style="margin-top:40px">To access another person's mailbox</h3>
      <ol class="dots">
        <li>Dial <b>5000.</b></li>
        <li>When prompted, enter the other person's extension number.</li>
        <li>Enter the voicemail PIN of the other person's mailbox, followed by <b>#.</b></li>
      </ol>
    </div>
    <div class="foot">www.telvanocommunications.com</div>
  </div>

  <div class="page right">
    <div class="brand"><div class="mark"></div><div class="name">TELVANO</div></div>
    <div class="tab">END-USER QUICK START GUIDE</div>
    <div class="content" style="top:86px">
      <h3 style="margin-top:0">Accessing Voicemail from the user portal</h3>
      <ul>
        <li>Start a web browser.</li>
        <li>Go to <b>phone.telvanocommunications.com</b></li>
      </ul>
      <div style="position:absolute;left:106px;top:82px;width:280px">
        <p style="text-align:left">Click in the Login name field and type your user name ______________________________(ext@customerdomain).</p>
        <p style="text-align:left;margin-top:8px">Your customerdomain typically is the same as your email address domain. Click in the Password field and enter your user password. (default password is ______________________</p>
      </div>
    </div>
    <div class="login"><div class="n">TELVANO</div><div class="f"></div><div class="f"></div><div class="btn"></div></div>
    <div class="icons"><div></div><div class="on"></div><div></div><div></div><div></div><div></div><div></div><div></div><div></div></div>
    <div class="msgs">
      <div class="bar">Messages</div>
      <div class="r" style="color:var(--blue)"><span>Voicemail &nbsp; Settings</span></div>
      <div class="r"><span style="flex:0 0 50px;border:1px solid #ccc">New</span></div>
      <div class="r" style="font-weight:700"><span></span><span>From</span><span></span><span>Date</span><span>Duration</span></div>
      <div class="r"><span style="color:var(--blue)">1 (555) 010-4412</span><span>MARLOW JANE</span><span></span><span>Feb 15th 11:05 am</span><span>0:35</span></div>
      <div class="r"><span style="color:var(--blue)">(555) 010-7730</span><span>Lakeview City</span><span></span><span>Feb 8th 10:54 am</span><span>0:16</span></div>
      <div class="r"><span style="color:var(--blue)">1 (555) 010-3385</span><span>OAKDALE</span><span></span><span>Feb 4th 8:50 am</span><span>0:11</span></div>
    </div>
    <div class="content" style="top:424px">
      <h3 style="margin-top:0">Record your greeting</h3>
      <ul>
        <li>From the <b>Settings</b> tab of the Messages page, click the speaker icon <span class="key"></span></li>
        <li>Next to <b>New Greeting</b>, click <b>Record</b> and the system will call you, or upload an existing greeting.</li>
      </ul>
    </div>
    <div class="foot">www.telvanocommunications.com</div>
  </div>
</section>

<section class="spread s3">
  <div class="page left">
    <div class="brand"><div class="mark"></div><div class="name">TELVANO</div></div>
    <div class="tab">END-USER QUICK START GUIDE</div>
    <div class="content">
      <div class="step" style="margin-bottom:8px">STEP 2: <span>Setting up the mobile application</span></div>
      <h3 style="margin-top:0">Installing Mobile Application</h3>
    </div>
    <div class="get"><div class="g">Get the app</div><div class="badge"></div><div class="badge"></div></div>
    <div style="position:absolute;left:21px;top:262px;font-size:7.6px;font-weight:700;color:var(--navy)">Search LinkDial and click install<span class="appicon"></span></div>
    <div class="shot" role="img" aria-label="Mobile app screenshot showing an active call screen" style="left:24px;top:305px;background:#2a2a2c"></div>
    <div class="shot" role="img" aria-label="Mobile app screenshot showing the LinkDial login form" style="left:122px;top:305px;background:#f2f3f5"></div>
    <div style="position:absolute;left:234px;top:365px;width:166px;font-size:7.6px;line-height:1.3">
      <h3 style="margin:0 0 4px">Zero Touch Configuration</h3>
      <p>To use LinkDial simply log-in with the credential from your PBX portal. That's all there is to it. All the features that you are accustomed to will pre-configured and ready for you.</p>
    </div>
    <div class="foot">www.telvanocommunications.com</div>
  </div>

  <div class="page right">
    <div class="brand"><div class="mark"></div><div class="name">TELVANO</div></div>
    <div class="tab">END-USER QUICK START GUIDE</div>
    <div class="content">
      <div class="step" style="margin-bottom:8px">STEP 3: <span>Using your desk phone</span></div>
      <h3 style="margin-top:0">Making Calls</h3>
      <p style="font-weight:600">Making a call with your phone does not require a leading 9. You can dial on-hook or off-hook.</p>
      <ol class="dots" style="margin-top:8px"><li><b>To dial on-hook</b></li></ol>
      <ul><li>Dial the phone number.</li><li>Pick up the handset, headset, or speaker.</li></ul>
      <ol class="dots" style="margin-top:8px"><li><b>To dial off-hook</b></li></ol>
      <ul><li>Pick up the handset, headset, or speaker.</li><li>Dial the phone number.</li><li>Calls to the US and Canada are all dialed using 10 or 11 digits.</li></ul>
      <h3 style="margin-top:22px">Receiving Calls</h3>
      <p style="font-weight:600">When a call comes in, you can answer it via a headset, speakerphone, or handset.</p>
      <ol class="dots">
        <li><b>To answer a call using a handset</b><br>– Lift the handset off-hook.</li>
        <li style="margin-top:3px"><b>To answer a call using a speakerphone</b><br>– Press the Speaker button.</li>
        <li style="margin-top:3px"><b>To answer a call using a headset</b><br>Usage depends on how the headset is connected. Often, you'll press the button on the headset or press the headset button on the phone.</li>
      </ol>
    </div>
    <div class="foot">www.telvanocommunications.com</div>
  </div>
</section>

<section class="spread s4">
  <div class="page left">
    <div class="brand"><div class="mark"></div><div class="name">TELVANO</div></div>
    <div class="tab">END-USER QUICK START GUIDE</div>
    <div class="content">
      <div class="step" style="font-family:Montserrat,sans-serif;font-size:12px;margin-bottom:8px">HANDLING CALLS</div>
      <p>Your cloud PBX features various ways to move calls around, including attended transfer, unattended (blind) transfer, voicemail transfer, park, and more. In this section, references to BLFs are the 1-touch buttons to extensions common at front-desk phones.</p>
      <h3 style="margin-top:22px">Attended Transfer</h3>
      <p>Attended transfer allows you to speak to the transfer recipient prior to completing the transfer while the caller is on hold.</p>
      <h4 style="margin-top:12px">To perform an attended transfer using Varnet and Corvana phones</h4>
      <ul>
        <li>Press the <b>Transfer key/softkey</b> <span class="key"></span> on your phone.</li>
        <li>Dial the recipient's extension or press their <b>BLF</b>.</li>
        <li>Speak to the recipient, and then either press <b>Transfer</b> <span class="key"></span> again to complete or cancel if the recipient cannot take the call.</li>
      </ul>
      <h3 style="margin-top:18px;margin-bottom:0">Blind Transfer</h3>
      <h4 style="margin-top:0">To blind transfer using Corvana phones</h4>
      <ul>
        <li>Press <b>Transfer</b> <span class="key"></span></li>
        <li>Dial the extension of the recipient.</li>
        <li>Press <b>Transfer</b> <span class="key"></span></li>
      </ul>
    </div>
    <div class="foot">www.telvanocommunications.com</div>
  </div>

  <div class="page right">
    <div class="brand"><div class="mark"></div><div class="name">TELVANO</div></div>
    <div class="tab">END-USER QUICK START GUIDE</div>
    <div class="content">
      <h3 style="margin-top:0">Transfers to External Numbers</h3>
      <p>A transfer can also go to an external number such as a cell phone. Follow the transfer directions above but instead of dialing an extension, dial a 10-digit phone number.</p>
      <h3 style="margin-top:14px">Park and Hold</h3>
      <p>On your phone system, hold is a local function. This means a call held on your phone cannot be picked up at another station. Park is a system-wide function. This means a call parked at one phone may be picked up by any phone.</p>
      <h4 style="margin-top:12px">To park a call</h4>
      <ul>
        <li>Dial *** in an active call from any phone. The system says, "The call is parked at 7xx."</li>
        <li>Hang up.</li>
        <li>To retrieve the parked call, dial <b>7xx</b> where xx is the number stated by the system.</li>
      </ul>
      <div class="step" style="font-family:Montserrat,sans-serif;font-size:12px;margin:34px 0 8px">EMERGENCY 911 CALLS</div>
      <ul>
        <li>When you dial 911 from LinkDial running on a mobile phone, the application will automatically dial out using your existing cellular service. 911 calls from your mobile phone will not be routed through your UCaaS service provider.</li>
        <li style="margin-top:8px">911 calls dialed from the desktop (WebRTC) app will be routed through your UCaaS service provider (the same as any other softphone).</li>
      </ul>
    </div>
    <div class="foot">www.telvanocommunications.com</div>
  </div>
</section>

</body>
</html>
```